Dental Office Looking for Modern, simple business cards

We just acquired our logo. Now we would like to make business cards. We are a dental office with two doctors. We are husband and wife and have a small boutique dental practice in a small town. We love our patients and they are always asking us to give our business cards to their friends. Please help us make business cards :-)

Target Market(s)

30-60 yr old

Industry/Entity Type

Dental Clinic

Contact Information for Business Card

Birch Hollow Dental P.C.
Family and Cosmetic Dentistry
4826 Delmore Rd. Pinecrest OH 12417
Tel: 555 642 7731 Fax: 555 642 7048

Dr. Tomas K. Brellin DDS
Dr. Marisol Ede Thornquist DDS

Font styles to use
Serif
Sans Serif

Requirements
Must have
• Simple clean design, modern, colorful. Should incorporate the logo.
Nice to have
• dental imagery ( teeth, smile, etc ...).

```html
<!DOCTYPE html>
<html lang="en">
<head>
<meta charset="utf-8">
<title>Birch Hollow Dental – Business Cards</title>
<link rel="stylesheet" href="https://fonts.googleapis.com/css2?family=Cinzel:wght@400;600&family=Open+Sans:wght@400;700&display=swap">
<style>
  :root {
    --backdrop: #d6d6d6;
    --card: #ffffff;
    --brand-blue: #2e7cc2;
    --brand-grey: #8a8d90;
    --ink-white: #ffffff;
    --shadow: rgba(0, 0, 0, 0.22);
  }
  * { box-sizing: border-box; margin: 0; padding: 0; }
  html, body {
    width: 1200px;
    height: 900px;
    overflow: hidden;
    background: var(--backdrop);
  }
  .canvas {
    position: relative;
    width: 1200px;
    height: 900px;
  }
  .card {
    position: absolute;
    left: 280px;
    width: 640px;
    height: 366px;
    background: var(--card);
    border-radius: 28px;
    box-shadow: 0 10px 24px var(--shadow);
    overflow: hidden;
  }
  .card--front { top: 52px; }
  .card--back { top: 470px; }

  /* Front: brand name */
  .brand {
    position: absolute;
    inset: 0;
    display: flex;
    align-items: center;
    justify-content: center;
    gap: 16px;
  }
  .brand__dot {
    width: 34px;
    height: 34px;
    border-radius: 50%;
    background: var(--brand-blue);
  }
  .brand__name {
    font-family: "Cinzel", serif;
    font-weight: 600;
    font-size: 40px;
    letter-spacing: 1px;
    color: var(--brand-blue);
  }

  /* Back */
  .doctors {
    position: absolute;
    top: 30px;
    right: 30px;
    text-align: right;
    font-family: "Cinzel", serif;
    font-weight: 400;
    font-size: 22px;
    line-height: 1.25;
    color: var(--brand-blue);
  }
  .doctors__title { color: var(--brand-grey); }
  .info-band {
    position: absolute;
    left: 255px;
    right: 0;
    top: 118px;
    height: 178px;
    background: var(--brand-blue);
    color: var(--ink-white);
    font-family: "Open Sans", sans-serif;
    text-align: right;
    padding: 22px 28px 0 20px;
  }
  .info-band__company,
  .info-band__tagline {
    font-weight: 700;
    font-size: 15px;
    text-transform: uppercase;
    line-height: 1.35;
  }
  .info-band__address {
    font-size: 15px;
    line-height: 1.5;
    margin-top: 2px;
  }
  .info-band__contact {
    font-size: 15px;
    margin-top: 16px;
  }
  .info-band__contact strong { font-weight: 700; }
  .info-band__divider { margin: 0 12px; }
  .back-brand {
    position: absolute;
    left: 34px;
    top: 190px;
    width: 200px;
    display: flex;
    align-items: center;
    gap: 12px;
  }
  .back-brand .brand__dot {
    flex: none;
    width: 26px;
    height: 26px;
  }
  .back-brand .brand__name {
    font-size: 24px;
    line-height: 1.15;
  }
</style>
</head>
<body>
<main class="canvas">
  <section class="card card--front" aria-label="Card front">
    <div class="brand">
      <span class="brand__dot"></span>
      <span class="brand__name">Birch Hollow Dental</span>
    </div>
  </section>

  <section class="card card--back" aria-label="Card back">
    <div class="doctors">
      <p>Dr. Tomas K. Brellin <span class="doctors__title">DDS</span></p>
      <p>Dr. Marisol Ede Thornquist <span class="doctors__title">DDS</span></p>
    </div>

    <div class="back-brand">
      <span class="brand__dot"></span>
      <span class="brand__name">Birch Hollow Dental</span>
    </div>

    <div class="info-band">
      <p class="info-band__company">Birch Hollow Dental P.C</p>
      <p class="info-band__tagline">Family and Cosmetic Dentistry</p>
      <p class="info-band__address">4826 Delmore Rd. Pinecrest OH 12417</p>
      <p class="info-band__contact">
        <strong>PHONE:</strong> 555 642 7731<span class="info-band__divider">|</span><strong>FAX:</strong> 555 642 7048
      </p>
    </div>
  </section>
</main>
</body>
</html>
```